6 - 8 'Holistic' Instagram Graphics

Hi there!
We are looking to build up a library of Graphic Templates to use as Instagram & Facebook posts for our Holistic Medi Spa (& 3 other companies eventually)
This competition is for a sample of 6 - 8 designs. For the winner(s), we will make an agreement for a batch order (Looking for 200+ designs in total), and will be looking to make a long term arrangement.
Please find a full job description in the attached Word Document.
Any questions, don't hesitate to ask.
Thanks!
Medical Spa

```html
<!DOCTYPE html>
<html lang="en">
<head>
<meta charset="utf-8">
<title>Willow Rest – Holistic Post Templates</title>
<link rel="stylesheet" href="https://fonts.googleapis.com/css2?family=Abril+Fatface&family=Playfair+Display:ital,wght@1,700&family=Oswald:wght@400;500&family=Josefin+Sans:wght@300;400;600&family=Dancing+Script:wght@500&family=Lato:ital,wght@0,300;0,400;1,400&display=swap">
<style>
  :root{
    --sand:#e7ddcc;
    --sand-deep:#d9cbb2;
    --mist:#eef6fa;
    --ink:#77745f;
    --ink-soft:#8d8a78;
    --peach:#e6bfa5;
    --frame:#7d7d7d;
    --paper:#ffffff;
  }
  *{box-sizing:border-box;margin:0;padding:0}
  html,body{width:678px;height:1200px;overflow:hidden;background:var(--paper)}
  .canvas{position:relative;width:678px;height:1200px;background:var(--paper)}
  .post{position:absolute;width:262px;height:262px;border:1px solid var(--frame);overflow:hidden;background:var(--paper)}
  .col-a{left:56px}.col-b{left:363px}
  .row-1{top:47px}.row-2{top:333px}.row-3{top:617px}.row-4{top:907px}
  .abs{position:absolute}
  .photo{position:absolute}
  .shape{position:absolute;inset:0;width:100%;height:100%}
  .footer{position:absolute;bottom:12px;font:400 5px/1 "Lato",sans-serif;letter-spacing:1.2px;color:var(--sand-deep);text-transform:uppercase;display:flex;align-items:center;gap:4px;white-space:nowrap}
  .footer .dot{width:5px;height:5px;border:1px solid var(--sand-deep);border-radius:50%}
  .serif-display{font-family:"Abril Fatface",serif}
  .serif-italic{font-family:"Playfair Display",serif;font-style:italic;font-weight:700}
  .condensed{font-family:"Oswald",sans-serif;text-transform:uppercase}
  .script{font-family:"Dancing Script",cursive}
  .nowrap{white-space:nowrap}

  /* giveaway */
  .giveaway .wash{left:0;bottom:0;width:262px;height:120px;background:var(--mist)}
  .giveaway .title{left:12px;top:168px;font-size:35px;color:var(--sand);line-height:1}
  .giveaway .lede{right:150px;top:203px;font-size:8.5px;color:var(--ink);line-height:1.4;text-align:right}
  .giveaway .prize{left:115px;top:211px;background:var(--sand);color:#fff;font-size:11px;padding:0 6px;line-height:14px}

  /* meditation */
  .meditation .wash{right:0;top:42px;width:200px;height:195px;background:var(--mist)}
  .meditation .kicker{left:0;font-size:9px;color:var(--ink);letter-spacing:.6px;padding:0 8px 2px 14px;border-bottom:1px solid var(--sand)}
  .meditation .k1{top:11px}.meditation .k2{top:32px}
  .meditation .mantra{left:162px;top:78px;font-size:17px;color:var(--ink);line-height:1.28}

  /* skincare */
  .skincare .wash{right:0;top:0;width:120px;height:262px;background:var(--mist)}
  .skincare .question{right:21px;top:22px;text-align:right;font-size:14.5px;line-height:20px;color:var(--sand)}

  /* cooking */
  .cooking .paper{left:16px;top:14px;width:230px;height:234px;background:#faf8f4}
  .cooking .number{left:32px;top:22px;font-size:74px;color:var(--sand);line-height:1}
  .cooking .rule{left:80px;top:105px;width:38px;border-top:1px solid var(--ink)}
  .cooking .headline{right:144px;top:111px;text-align:right;font-size:11px;line-height:1.25;color:var(--ink)}
  .cooking .body{right:171px;top:164px;text-align:right;font:italic 400 5.6px/1.6 "Lato",serif;color:var(--ink)}

  /* fact */
  .fact .card{left:42px;top:46px;width:174px;height:178px;background:#fff;box-shadow:6px 6px 0 -1px #fff,6px 6px 0 0 var(--ink-soft)}
  .fact .tag{left:46px;top:50px;width:150px;height:22px;background:var(--mist);font-size:15px;color:var(--sand-deep);padding-left:6px;line-height:22px}
  .fact .statement{left:42px;top:84px;width:174px;text-align:center;font:300 15.5px/22px "Josefin Sans",sans-serif;color:var(--ink);letter-spacing:.8px}

  /* testimonial */
  .review .wash{inset:0;background:var(--mist)}
  .review .bubble{left:46px;top:44px;width:171px;height:172px;background:#fff;border-radius:4px}
  .review .heading{left:46px;top:54px;width:171px;text-align:center;font-size:14px;color:var(--ink);letter-spacing:.4px}
  .review .quote{left:57px;top:88px;width:148px;font:300 5.6px/8.5px "Lato",sans-serif;color:var(--ink);text-align:justify;letter-spacing:.2px}
  .review .author{display:block;text-align:right;font-family:"Dancing Script",cursive;color:var(--peach);font-size:7px}
  .review .stars{left:92px;top:186px;display:flex}
  .review .contact{left:0;width:262px;text-align:center;font:400 5px/1.6 "Lato",sans-serif;letter-spacing:1.2px;color:var(--sand-deep);top:232px}

  /* gift */
  .gift .wash{left:0;top:0;width:262px;height:218px;background:var(--mist)}
  .gift .headline{left:132px;top:82px;font:400 20px/26px "Josefin Sans",sans-serif;color:var(--ink);letter-spacing:.3px;white-space:nowrap}
  .gift .details{left:132px;top:166px;font-size:10px;line-height:14px;color:var(--ink);letter-spacing:.9px;white-space:nowrap}

  /* offer */
  .offer .ribbon{left:34px;top:0;width:70px;height:110px}
  .offer .ribbon-text{left:34px;top:36px;width:70px;text-align:center;color:var(--ink)}
  .offer .r1{font-size:8.5px;letter-spacing:.6px;display:block;line-height:12px}
  .offer .r2{font-family:"Abril Fatface",serif;font-size:17px;line-height:21px;display:block}
</style>
</head>
<body>
<main class="canvas">

  <section class="post giveaway col-a row-1">
    <div class="abs wash"></div>
    <svg class="shape" viewBox="0 0 262 262" role="img" aria-label="Photo of a woman relaxing during a facial treatment">
      <defs><linearGradient id="g-facial" x1="0" y1="0" x2="1" y2="1"><stop offset="0" stop-color="#f4ece4"/><stop offset="1" stop-color="#d8b59c"/></linearGradient></defs>
      <path d="M86 0H262V196H120C132 150 96 120 110 78C118 52 92 30 86 0Z" fill="url(#g-facial)"/>
    </svg>
    <div class="abs title serif-display nowrap">Giveaway</div>
    <div class="abs lede serif-italic nowrap">Share this post with<br>a friend &amp; win a</div>
    <div class="abs prize script nowrap">free treatment</div>
    <div class="footer" style="right:12px"><span class="dot"></span>hello@willowrest.com</div>
  </section>

  <section class="post meditation col-b row-1">
    <div class="abs wash"></div>
    <div class="abs kicker k1 condensed nowrap">Meditation is</div>
    <div class="abs kicker k2 condensed nowrap">Hanging out with your soul</div>
    <svg class="shape" viewBox="0 0 262 262" role="img" aria-label="Photo of a person meditating by the sea">
      <defs><linearGradient id="g-med" x1="0" y1="0" x2="0" y2="1"><stop offset="0" stop-color="#e3e0d8"/><stop offset="1" stop-color="#5b3a22"/></linearGradient></defs>
      <path d="M0 52H118C102 80 104 102 124 112C104 128 108 170 136 190C130 232 90 262 50 262H0Z" fill="url(#g-med)"/>
    </svg>
    <div class="abs mantra serif-display nowrap">slow<br>down<br>-<br>just<br>breathe...</div>
    <div class="footer" style="right:14px"><span class="dot"></span>hello@willowrest.com</div>
  </section>

  <section class="post skincare col-a row-2">
    <div class="abs wash"></div>
    <svg class="shape" viewBox="0 0 262 262" role="img" aria-label="Photo of a woman with a headband enjoying a skincare treatment">
      <defs><linearGradient id="g-skin" x1="0" y1="0" x2="1" y2="1"><stop offset="0" stop-color="#e9e4df"/><stop offset="1" stop-color="#c99f86"/></linearGradient></defs>
      <path d="M0 0H140C128 30 120 62 136 92C112 116 114 150 150 172C176 200 176 236 150 262H0Z" fill="url(#g-skin)"/>
    </svg>
    <div class="abs question serif-display nowrap">When did<br>you last<br>consider<br>your<br>skincare<br>routine?</div>
  </section>

  <section class="post cooking col-b row-2">
    <div class="abs paper"></div>
    <svg class="shape" viewBox="0 0 262 262" role="img" aria-label="Photo of a rice bowl with shredded meat and lime on a wooden table">
      <defs><linearGradient id="g-food" x1="0" y1="0" x2="1" y2="1"><stop offset="0" stop-color="#c9dbe3"/><stop offset="1" stop-color="#9fb9c6"/></linearGradient></defs>
      <rect x="98" y="14" width="148" height="234" fill="url(#g-food)"/>
      <circle cx="172" cy="190" r="56" fill="#f4f1ec"/>
    </svg>
    <div class="abs number serif-display">10</div>
    <div class="abs rule"></div>
    <div class="abs headline serif-italic nowrap">best cooking<br>tips for special<br>ocasions</div>
    <div class="abs body nowrap">Lorem ipsum dolor sit<br>amet, consectetur<br>adipiscing elit.<br>Suspendisse nunc leo,<br>consequat quis<br>malesuada nec.</div>
  </section>

  <section class="post fact col-a row-3">
    <div class="photo" role="img" aria-label="Photo of an athletic woman in sportswear" style="left:130px;top:0;width:132px;height:262px;background:linear-gradient(160deg,#b8a89a,#6d5b4f)"></div>
    <div class="abs card"></div>
    <div class="abs tag script nowrap">Did you know?...</div>
    <div class="abs statement nowrap">EMS Body<br>Sculpting is<br>equivalent to<br>16 weeks HIT<br>Training?</div>
    <div class="footer" style="left:28px"><span>www.willowrest.com</span><span class="dot"></span></div>
  </section>

  <section class="post review col-b row-3">
    <div class="abs wash"></div>
    <div class="abs bubble"></div>
    <svg class="abs" style="left:60px;top:214px" width="18" height="12" viewBox="0 0 18 12"><path d="M0 0H18L4 12Z" fill="#fff"/></svg>
    <div class="abs heading serif-display">testimonial</div>
    <p class="abs quote">It's my first time to go to Willow Rest. But I received a very welcoming treatment from Ma'm Lena and she did a very professional way of telling me my treatment. And I will go and continue to support their business. And also I will recommend Willow Rest to my friend who want to have their skin treated. Well done Willow Rest. I will see you in a month time. Thank you for the nice treatment. <span class="author">Clara Meadow</span></p>
    <div class="abs stars">
      <svg width="74" height="12" viewBox="0 0 74 12"><g fill="var(--sand)"><path id="st" d="M6 0L7.6 4.2H12L8.4 6.8L9.8 11L6 8.4L2.2 11L3.6 6.8L0 4.2H4.4Z"/><use href="#st" x="15"/><use href="#st" x="30"/><use href="#st" x="45"/><use href="#st" x="60"/></g></svg>
    </div>
    <div class="photo" role="img" aria-label="Watercolour green leaves illustration" style="left:196px;top:140px;width:55px;height:115px;border-radius:50% 50% 40% 40%;background:linear-gradient(180deg,#b7cfc4,#7fa497);opacity:.8"></div>
    <div class="abs contact">+1 (555) 010-2040<br>hello@willowrest.com</div>
  </section>

  <section class="post gift col-a row-4">
    <div class="abs wash"></div>
    <div class="photo" role="img" aria-label="Photo of a bowl of ayurvedic greens and rice" style="left:20px;top:62px;width:95px;height:95px;background:#fff;padding:6px">
      <div style="width:100%;height:100%;background:radial-gradient(circle at 70% 50%,#c9a53a 0 35%,#5f7a3a 55%,#efe9e3 60%)"></div>
    </div>
    <div class="photo" role="img" aria-label="Watercolour eucalyptus leaves illustration" style="left:195px;top:0;width:67px;height:62px;background:linear-gradient(200deg,#8fae98,#d4e2d6);border-radius:0 0 0 60%"></div>
    <div class="abs headline">WE HAVE<br>A GIFT FOR<br>YOU!</div>
    <div class="abs details condensed">Enjoy a free<br>ayurvedic recipe<br>book &amp; meal plan</div>
    <div class="footer" style="left:86px"><span>www.willowrest.com</span><span class="dot"></span></div>
  </section>

  <section class="post offer col-b row-4">
    <div class="photo" role="img" aria-label="Photo of the spa treatment lounge with reclining chairs" style="left:16px;top:35px;width:231px;height:178px;background:linear-gradient(180deg,#e6ebe8 0%,#d7d3cb 55%,#9b7d62 100%)"></div>
    <svg class="abs ribbon" viewBox="0 0 70 110"><path d="M0 0H70V110L35 98L0 110Z" fill="var(--sand)"/></svg>
    <div class="abs ribbon-text"><span class="r1 condensed">Only today</span><span class="r2">20%<br>OFF</span></div>
    <div class="footer" style="left:86px"><span>www.willowrest.com</span><span class="dot"></span></div>
  </section>

</main>
</body>
</html>
```